TK & LJ Shearing Pty Ltd

We already have an existing logo created by Lumen Guild however we have restructured to a company. We would like someone to add Pty Ltd to our business name please.

Colors

Designer to choose only greyscale colors for use in the design.

```html
<!DOCTYPE html>
<html lang="en">
<head>
<meta charset="UTF-8">
<title>TK &amp; LJ Shearing Pty Ltd — Business Card</title>
<link rel="stylesheet" href="https://fonts.googleapis.com/css2?family=Cinzel:wght@400;700&family=Raleway:wght@300;400&display=swap">
<style>
  :root {
    --backdrop: #d6d4d0;
    --card-top: #2e2e2e;
    --card-bottom: #0d0d0d;
    --ink: #f2f2f2;
    --ink-soft: #cfcfcf;
    --rule: #8a8a8a;
    --icon-bg: #e6e6e6;
    --icon-fg: #111111;
  }
  * { box-sizing: border-box; margin: 0; padding: 0; }
  html, body {
    width: 1200px;
    height: 1022px;
    overflow: hidden;
    background: var(--backdrop);
  }
  .stage {
    width: 1200px;
    height: 1022px;
    display: flex;
    align-items: center;
    justify-content: center;
  }
  .business-card {
    width: 900px;
    height: 515px;
    border-radius: 18px;
    background: linear-gradient(160deg, var(--card-top) 0%, #1a1a1a 45%, var(--card-bottom) 100%);
    box-shadow: 0 18px 40px rgba(0,0,0,0.35);
    display: flex;
    align-items: center;
    padding: 0 70px;
    color: var(--ink);
  }
  .brand {
    flex: 0 0 390px;
    display: flex;
    flex-direction: column;
    align-items: flex-start;
    gap: 10px;
  }
  .brand-mark {
    width: 26px;
    height: 26px;
    border-radius: 50%;
    background: var(--ink);
  }
  .brand-name {
    font-family: 'Cinzel', serif;
    font-weight: 700;
    font-size: 44px;
    line-height: 1.1;
    letter-spacing: 1px;
    color: var(--ink);
  }
  .divider {
    width: 1px;
    height: 170px;
    background: var(--rule);
    margin: 0 40px 0 20px;
  }
  .contact {
    display: flex;
    flex-direction: column;
    gap: 14px;
  }
  .contact-name {
    font-family: 'Cinzel', serif;
    font-weight: 400;
    font-size: 30px;
    letter-spacing: 3px;
    color: var(--ink);
    margin-bottom: 8px;
  }
  .contact-line {
    display: flex;
    align-items: center;
    gap: 12px;
    font-family: 'Raleway', sans-serif;
    font-weight: 300;
    font-size: 21px;
    color: var(--ink-soft);
  }
  .contact-icon {
    width: 20px;
    height: 20px;
    flex: 0 0 20px;
  }
</style>
</head>
<body>
<main class="stage">
  <section class="business-card">
    <div class="brand">
      <span class="brand-mark" aria-hidden="true"></span>
      <h1 class="brand-name">TK &amp; LJ Shearing Pty Ltd</h1>
    </div>
    <div class="divider" aria-hidden="true"></div>
    <div class="contact">
      <p class="contact-name">Sam Whitford</p>
      <p class="contact-line">
        <svg class="contact-icon" viewBox="0 0 20 20" aria-hidden="true">
          <circle cx="10" cy="10" r="10" fill="var(--icon-bg)"/>
          <path d="M5 10.5 L10 6 L15 10.5 M7 9.5 V14 H13 V9.5" fill="none" stroke="var(--icon-fg)" stroke-width="1.5" stroke-linejoin="round"/>
        </svg>
        PO Box 418 Carrow WA 6512
      </p>
      <p class="contact-line">
        <svg class="contact-icon" viewBox="0 0 20 20" aria-hidden="true">
          <circle cx="10" cy="10" r="10" fill="var(--icon-bg)"/>
          <path d="M7 5.5 C6 6.5 6 8.5 8 11 C10 13.5 12.5 14.5 13.8 13.5 L12.3 11.6 L11 12.2 C10 11.6 8.8 10.3 8.3 9.2 L9 8 Z" fill="var(--icon-fg)"/>
        </svg>
        0400 118 725
      </p>
      <p class="contact-line">
        <svg class="contact-icon" viewBox="0 0 20 20" aria-hidden="true">
          <circle cx="10" cy="10" r="10" fill="var(--icon-bg)"/>
          <rect x="5" y="6.5" width="10" height="7" fill="none" stroke="var(--icon-fg)" stroke-width="1.3"/>
          <path d="M5 6.5 L10 10.5 L15 6.5" fill="none" stroke="var(--icon-fg)" stroke-width="1.3"/>
        </svg>
        tkljshearing@mailbox.com
      </p>
    </div>
  </section>
</main>
</body>
</html>
```